Business Card Design Project

We are a construction company in Orange County, CA. We need a two sided business card. We would like the back to be our logo with web URL. Front should included Name, title, address, phone, fax and email address.

our address is
387 West Marlowe Blvd, Suite 402
Brookhaven, CA 92740

Our logo files are attached.

Construction

```html
<!DOCTYPE html>
<html lang="en">
<head>
<meta charset="utf-8">
<title>Verant Business Card</title>
<link rel="stylesheet" href="https://fonts.googleapis.com/css2?family=Crimson+Text:wght@400;700&display=swap">
<style>
  :root {
    --navy: #1d4a80;
    --ink: #2b2b2b;
    --charcoal: #3a3a3c;
    --rule: #c9c9c9;
    --paper: #ffffff;
    --backdrop: #e6e7e9;
  }
  * { box-sizing: border-box; margin: 0; padding: 0; }
  html, body { width: 1200px; height: 900px; overflow: hidden; }
  body {
    background: var(--backdrop);
    font-family: "Crimson Text", Georgia, serif;
    position: relative;
  }
  .card {
    position: absolute;
    width: 640px;
    height: 366px;
    border-radius: 22px;
    overflow: hidden;
    box-shadow: 0 6px 18px rgba(0,0,0,.18);
  }
  /* Back side */
  .card-back {
    left: 60px; top: 60px;
    background: var(--navy);
    display: flex; align-items: center; justify-content: center;
  }
  .card-back .brand-name {
    color: var(--paper);
    font-size: 124px;
    font-weight: 700;
    letter-spacing: 2px;
    line-height: 1;
  }
  /* Front side */
  .card-front {
    left: 500px; top: 470px;
    background: var(--paper);
  }
  .card-front .brand-name {
    position: absolute; left: 30px; top: 22px;
    color: var(--navy);
    font-size: 66px;
    font-weight: 700;
    letter-spacing: 1px;
    line-height: 1;
  }
  .name-marker {
    position: absolute; left: 0; top: 130px;
    width: 6px; height: 36px;
    background: var(--navy);
    border-radius: 0 3px 3px 0;
  }
  .person { position: absolute; left: 34px; top: 126px; }
  .person-name { font-size: 25px; color: var(--ink); line-height: 1.1; white-space: nowrap; }
  .person-title { font-size: 15px; font-weight: 700; color: var(--navy); }
  .divider {
    position: absolute; left: 34px; right: 26px; top: 192px;
    border-top: 1px solid var(--rule);
  }
  .contact {
    position: absolute; display: flex; align-items: center; gap: 10px;
    font-size: 18px; color: var(--ink); white-space: nowrap; line-height: 1.3;
  }
  .contact svg { width: 16px; height: 16px; fill: var(--navy); flex: none; }
  .phone { left: 34px; top: 200px; }
  .email { left: 34px; top: 236px; }
  .mobile { left: 250px; top: 214px; }
  .fax { left: 250px; top: 246px; }
  .address {
    position: absolute; left: 405px; top: 236px;
    font-size: 15.5px; line-height: 1.3; color: var(--navy);
    white-space: nowrap;
  }
  .footer-band { position: absolute; left: 0; bottom: 0; width: 640px; height: 70px; }
  .web {
    position: absolute; right: 24px; bottom: 12px;
    font-size: 19px; color: var(--paper); white-space: nowrap;
  }
</style>
</head>
<body>
  <section class="card card-back" aria-label="Card back">
    <span class="brand-name">VERANT</span>
  </section>

  <section class="card card-front" aria-label="Card front">
    <span class="brand-name">VERANT</span>

    <span class="name-marker"></span>
    <div class="person">
      <p class="person-name">Marcus. D . Holloway</p>
      <p class="person-title">General Manager</p>
    </div>

    <div class="divider"></div>

    <p class="contact phone">
      <svg viewBox="0 0 24 24"><path d="M6.6 10.8a15 15 0 0 0 6.6 6.6l2.2-2.2c.3-.3.7-.4 1-.2 1.1.4 2.3.6 3.6.6.6 0 1 .4 1 1V20c0 .6-.4 1-1 1A17 17 0 0 1 3 4c0-.6.4-1 1-1h3.5c.6 0 1 .4 1 1 0 1.3.2 2.5.6 3.6.1.3 0 .7-.2 1z"/></svg>
      (00) 4821 7390
    </p>
    <p class="contact email">
      <svg viewBox="0 0 24 24"><path d="M2 5h20v14H2zm2 2v.5l8 5 8-5V7z"/></svg>
      info@verantbuild.com
    </p>
    <p class="contact mobile">
      <svg viewBox="0 0 24 24"><path d="M7 1h10a2 2 0 0 1 2 2v18a2 2 0 0 1-2 2H7a2 2 0 0 1-2-2V3a2 2 0 0 1 2-2zm0 3v14h10V4z"/></svg>
      05512 348 900
    </p>
    <p class="contact fax">
      <svg viewBox="0 0 24 24"><path d="M3 3h18v18H3zm3 3v5h12V6zm0 8v2h3v-2zm5 0v2h3v-2zm5 0v2h2v-2z"/></svg>
      05512 348 900
    </p>
    <p class="address">387 West Marlowe Blvd, Suite 402<br>Brookhaven, CA 92740</p>

    <svg class="footer-band" viewBox="0 0 640 70" preserveAspectRatio="none" aria-hidden="true">
      <polygon points="0,8 440,30 640,30 640,70 0,70" fill="var(--navy)"/>
      <polygon points="420,22 640,22 640,70 442,70" fill="var(--charcoal)"/>
    </svg>
    <p class="web">www.verantbuild.com</p>
  </section>
</body>
</html>
```